Business Card needed for Drainora, a growing Septic Service company

Drainora, a growing local septic service company in Pennsylvania, needs updated business cards. We'd like the business card to feature our logo and communicate that we provide Septic Pumping, Installations/Repairs, Restroom Rentals, and 24/7 Emergency Service. The business card should be eye-catching, bold, and clean/simple. We have been in business almost 10 years and would like to expand and update our business brand and image.

Target Market(s)

Residential and Commercial, New and Current Homeowners

Industry/Entity Type

Service

Contact Information for Business Card

Contact on the business card should be: Dale Pruitt Owner & Operator
Phone: 610-555-0187
Email: service@drainora.example
Website: www.drainora.example
Address: 812 Birchwell Lane Easton PA 18042

Font styles to use
Sans Serif

Colors

Designer to choose colors to be used in the design.

Requirements
Must have
• Feature logo on both side of business card.
Nice to have
• We envision the contact information on one side and our services listed on the other side. Utilize the green from the symbol in our logo as part of the design, overall design color scheme should be white, grey, black.

```html
<!DOCTYPE html>
<html lang="en">
<head>
<meta charset="utf-8">
<title>Drainora Business Card</title>
<link href="https://fonts.googleapis.com/css2?family=Montserrat:wght@400;500;700;800&display=swap" rel="stylesheet">
<style>
  :root {
    --bg: #adaeaa;
    --card-white: #f4f4f2;
    --card-black: #202020;
    --ink: #1a1a1a;
    --green: #7cc242;
    --white: #ffffff;
  }
  * { margin: 0; padding: 0; box-sizing: border-box; }
  html, body { width: 1200px; height: 801px; overflow: hidden; }
  body {
    background: var(--bg);
    font-family: "Montserrat", sans-serif;
    display: flex;
    align-items: center;
    justify-content: center;
    gap: 40px;
  }
  .card {
    width: 540px;
    height: 309px;
    position: relative;
    border-bottom: 4px solid var(--green);
    box-shadow: 0 14px 30px rgba(0,0,0,0.22);
  }

  /* Contact side */
  .card--contact {
    background: var(--card-white);
    display: flex;
    align-items: center;
    padding: 0 30px 0 30px;
  }
  .brand {
    display: flex;
    align-items: center;
    gap: 10px;
  }
  .brand__square {
    width: 30px;
    height: 30px;
    background: var(--green);
    flex: none;
  }
  .brand__name {
    font-weight: 800;
    text-transform: uppercase;
    letter-spacing: 0.5px;
    color: var(--ink);
    font-size: 30px;
    line-height: 1;
  }
  .card--contact .brand { width: 232px; flex: none; }
  .divider {
    width: 2px;
    height: 150px;
    background: var(--green);
    margin: 0 24px 0 10px;
    flex: none;
  }
  .contact { color: var(--ink); font-size: 13px; line-height: 1.45; white-space: nowrap; }
  .contact__name {
    color: var(--green);
    font-weight: 800;
    font-size: 19px;
    text-transform: uppercase;
    letter-spacing: 0.5px;
    line-height: 1.1;
  }
  .contact__role { margin-bottom: 2px; }
  .contact__line { display: flex; align-items: center; gap: 7px; }
  .contact__icon { width: 10px; height: 10px; flex: none; }

  /* Services side */
  .card--services {
    background: var(--card-black);
    display: flex;
    flex-direction: column;
    align-items: center;
    justify-content: center;
    gap: 34px;
  }
  .card--services .brand { gap: 16px; }
  .card--services .brand__square { width: 56px; height: 56px; }
  .card--services .brand__name { color: var(--white); font-size: 54px; }
  .services {
    list-style: none;
    color: var(--white);
    font-size: 15px;
    font-weight: 500;
    display: flex;
    flex-wrap: wrap;
    justify-content: center;
    column-gap: 14px;
    row-gap: 4px;
    width: 420px;
  }
  .services__item { display: flex; align-items: center; gap: 7px; }
  .services__item::before {
    content: "";
    width: 10px;
    height: 10px;
    background: var(--green);
  }
</style>
</head>
<body>
  <section class="card card--contact" aria-label="Business card contact side">
    <div class="brand">
      <span class="brand__square"></span>
      <span class="brand__name">Drainora</span>
    </div>
    <span class="divider"></span>
    <div class="contact">
      <p class="contact__name">Dale Pruitt</p>
      <p class="contact__role">Owner &amp; Operator</p>
      <p>812 Birchwell Lane</p>
      <p>Alder Falls PA 19990</p>
      <p class="contact__line">
        <svg class="contact__icon" viewBox="0 0 24 24" aria-hidden="true"><path fill="#7cc242" d="M6.6 10.8a15 15 0 0 0 6.6 6.6l2.2-2.2c.3-.3.7-.4 1-.2 1.1.4 2.3.6 3.6.6.6 0 1 .4 1 1V20c0 .6-.4 1-1 1A17 17 0 0 1 3 4c0-.6.4-1 1-1h3.5c.6 0 1 .4 1 1 0 1.3.2 2.5.6 3.6.1.3 0 .7-.2 1z"/></svg>
        610-555-0187
      </p>
      <p class="contact__line">
        <svg class="contact__icon" viewBox="0 0 24 24" aria-hidden="true"><rect x="2" y="5" width="20" height="14" fill="none" stroke="#7cc242" stroke-width="2.4"/><path d="M2 6l10 7 10-7" fill="none" stroke="#7cc242" stroke-width="2.4"/></svg>
        service@drainora.example
      </p>
      <p class="contact__line">
        <svg class="contact__icon" viewBox="0 0 24 24" aria-hidden="true"><g fill="none" stroke="#7cc242" stroke-width="2"><circle cx="12" cy="12" r="10"/><ellipse cx="12" cy="12" rx="4.5" ry="10"/><path d="M2 12h20M4 7h16M4 17h16"/></g></svg>
        www.drainora.example
      </p>
    </div>
  </section>

  <section class="card card--services" aria-label="Business card services side">
    <div class="brand">
      <span class="brand__square"></span>
      <span class="brand__name">Drainora</span>
    </div>
    <ul class="services">
      <li class="services__item">Septic Pumping</li>
      <li class="services__item">Installations/Repairs</li>
      <li class="services__item">Restroom Rentals</li>
      <li class="services__item">24/7 Emergency</li>
    </ul>
  </section>
</body>
</html>
```